Security Business card

I need a new business card for my new company Bastion Crest Security Group we provide security for clubs,pubs,hotels etc. I would like to see the main colors red and black to be used. The final design should communicate honor and integrity.

Industry/Entity Type

Security

Contact Information for Business Card

Marcus Delvane
Company Name-Bastion Crest Security Group
Abn-47318265094
Acn-318265094
address- po box 7352 Ferndale nsw 2291
phone- 0437682915
email- Marcus@bastioncrest.com.au

```html
<!DOCTYPE html>
<html lang="en">
<head>
<meta charset="utf-8">
<title>Bastion Crest Security Group – Business Card</title>
<link href="https://fonts.googleapis.com/css2?family=Lato:wght@400;700;900&display=swap" rel="stylesheet">
<style>
  :root {
    --backdrop: #2a2a2c;
    --card-top: #ffffff;
    --card-bottom: #ececec;
    --brand-red: #c41e2a;
    --brand-red-dark: #a0141e;
    --ink: #1e1e1e;
    --white: #ffffff;
    --faint-red: rgba(196, 30, 42, 0.12);
  }
  * { box-sizing: border-box; margin: 0; padding: 0; }
  html, body {
    width: 1200px;
    height: 900px;
    overflow: hidden;
    background: var(--backdrop);
    font-family: "Lato", Arial, sans-serif;
  }
  .canvas {
    position: relative;
    width: 1200px;
    height: 900px;
    display: flex;
    align-items: center;
    justify-content: center;
  }
  .business-card {
    position: relative;
    width: 1000px;
    height: 580px;
    border-radius: 30px;
    overflow: hidden;
    background: linear-gradient(180deg, var(--card-top), var(--card-bottom));
    box-shadow: 0 20px 50px rgba(0, 0, 0, 0.55);
  }
  .header-band {
    position: absolute;
    top: 0; left: 0; right: 0;
    height: 112px;
    background: linear-gradient(180deg, var(--brand-red), var(--brand-red-dark));
    text-align: right;
    padding: 22px 48px 0 0;
    color: var(--white);
  }
  .holder-name {
    font-weight: 900;
    font-size: 42px;
    letter-spacing: 1px;
    line-height: 1;
    text-transform: uppercase;
  }
  .holder-title {
    font-weight: 700;
    font-size: 20px;
    letter-spacing: 1.5px;
    margin-top: 6px;
    text-transform: uppercase;
  }
  .company-block {
    position: absolute;
    top: 138px;
    right: 48px;
    text-align: right;
  }
  .company-name {
    font-weight: 900;
    font-size: 32px;
    color: var(--brand-red);
    text-transform: uppercase;
    line-height: 1.1;
  }
  .company-registration {
    font-weight: 700;
    font-size: 21px;
    color: var(--ink);
    margin-top: 2px;
  }
  .brand-mark {
    position: absolute;
    top: 200px;
    left: 70px;
    display: flex;
    align-items: center;
    gap: 16px;
  }
  .brand-mark-dot {
    width: 46px;
    height: 46px;
    border-radius: 50%;
    background: var(--brand-red);
  }
  .brand-mark-name {
    font-weight: 900;
    font-size: 40px;
    line-height: 1.05;
    color: var(--ink);
    text-transform: uppercase;
  }
  .brand-watermark {
    position: absolute;
    top: 190px;
    right: 60px;
    width: 260px;
    height: 260px;
    border-radius: 50%;
    background: var(--faint-red);
  }
  .tagline {
    position: absolute;
    right: 48px;
    bottom: 150px;
    font-weight: 900;
    font-size: 28px;
    color: var(--brand-red);
    text-transform: uppercase;
  }
  .contact-list {
    position: absolute;
    left: 70px;
    bottom: 40px;
    list-style: none;
  }
  .contact-item {
    display: flex;
    align-items: center;
    gap: 16px;
    font-weight: 700;
    font-size: 27px;
    color: var(--ink);
    margin-top: 10px;
  }
  .contact-icon {
    width: 28px;
    height: 28px;
    fill: var(--brand-red);
    flex: none;
  }
</style>
</head>
<body>
<main class="canvas">
  <article class="business-card">
    <header class="header-band">
      <div class="holder-name">Marcus Delvane</div>
      <div class="holder-title">Director</div>
    </header>

    <div class="brand-watermark" aria-hidden="true"></div>

    <div class="company-block">
      <div class="company-name">Bastion Crest Security Group</div>
      <div class="company-registration">Abn-47318265094 Acn-318265094</div>
    </div>

    <div class="brand-mark">
      <span class="brand-mark-dot" aria-hidden="true"></span>
      <span class="brand-mark-name">Bastion<br>Crest</span>
    </div>

    <div class="tagline">Security for Clubs,Pubs,Hotels</div>

    <ul class="contact-list">
      <li class="contact-item">
        <svg class="contact-icon" viewBox="0 0 24 24" aria-hidden="true">
          <path d="M3 8c0-3 4-5 9-5s9 2 9 5v2h-5V8c-1-1-7-1-8 0v2H3z"/>
          <path d="M7 12h10l3 8H4z"/>
        </svg>
        0437682915
      </li>
      <li class="contact-item">
        <svg class="contact-icon" viewBox="0 0 24 24" aria-hidden="true">
          <path d="M2 5h20v14H2z M3.5 6.5 12 13l8.5-6.5" stroke="#fff" stroke-width="1.4"/>
        </svg>
        Marcus@bastioncrest.com.au
      </li>
      <li class="contact-item">
        <svg class="contact-icon" viewBox="0 0 24 24" aria-hidden="true">
          <path d="M12 3 1 12h3v9h6v-6h4v6h6v-9h3z"/>
        </svg>
        PO Box 7352 Ferndale NSW 2291
      </li>
    </ul>
  </article>
</main>
</body>
</html>
```